label design peanut butter jar to be marketed internationally for a singapore based company

We need design of 2 labels creamy peanut butter and crunch peanut butter
The design is the same only photo of product
And wording change
The logo norvale remains the same and has to be used logo of peanut has to be used
Some idea designs by our in house designer
Enclosed .
Plus a design of a competitor silver orchard

Target Market(s)

international specially emerging markets

Industry/Entity Type

It Company

Requirements
Must have
• norvale logo
• peanut logo

```html
<!DOCTYPE html>
<html lang="en">
<head>
<meta charset="utf-8">
<title>Norvale Creamy Peanut Butter – Jar Label</title>
<link rel="stylesheet" href="https://fonts.googleapis.com/css2?family=Arimo:wght@700&display=swap">
<style>
  :root {
    --canvas: #f4f4f2;
    --purple: #5a2d86;
    --orange: #f26b1d;
    --orange-light: #f9a43a;
    --yellow: #fff200;
    --white: #ffffff;
    --ink: #111111;
    --peanut: #d59b5c;
    --peanut-dark: #b57a3f;
  }
  html, body {
    margin: 0;
    width: 871px;
    height: 1200px;
    overflow: hidden;
    background: var(--canvas);
  }
  .label {
    position: absolute;
    left: 35px;
    top: 219px;
    width: 800px;
    height: 761px;
    font-family: "Arimo", Arial, sans-serif;
    font-weight: 700;
  }
  .brand-name { fill: var(--purple); font-size: 62px; letter-spacing: 9px; }
  .burst-text { fill: var(--ink); font-size: 14px; }
  .variant-main { fill: var(--purple); font-size: 50px; }
  .variant-sub { fill: var(--purple); font-size: 29px; }
  .net-weight { fill: var(--white); font-size: 17px; }
</style>
</head>
<body>
<svg class="label" viewBox="0 0 620 590" xmlns="http://www.w3.org/2000/svg">
  <defs>
    <radialGradient id="sunburst" cx="0.5" cy="0.45" r="0.6">
      <stop offset="0" stop-color="#fde27a"/>
      <stop offset="0.45" stop-color="var(--orange-light)"/>
      <stop offset="1" stop-color="var(--orange)"/>
    </radialGradient>
    <radialGradient id="product-tones" cx="0.5" cy="0.5" r="0.7">
      <stop offset="0" stop-color="var(--peanut)"/>
      <stop offset="1" stop-color="var(--peanut-dark)"/>
    </radialGradient>
    <clipPath id="label-area"><rect width="620" height="590"/></clipPath>
  </defs>

  <g clip-path="url(#label-area)">
    <rect class="label-ground" width="620" height="590" fill="var(--purple)"/>
    <ellipse class="sun-panel" cx="310" cy="285" rx="300" ry="292" fill="url(#sunburst)" stroke="var(--yellow)" stroke-width="6"/>

    <rect class="top-band" x="0" y="0" width="620" height="22" fill="var(--purple)"/>
    <rect class="bottom-band" x="0" y="512" width="620" height="78" fill="var(--purple)"/>

    <rect class="product-photo" x="150" y="190" width="300" height="220" rx="28"
          fill="url(#product-tones)"
          role="img" aria-label="Product photo: a spoon heaped with creamy peanut butter"/>

    <ellipse class="brand-oval" cx="305" cy="112" rx="232" ry="70" fill="var(--white)" stroke="var(--orange)" stroke-width="6"/>
    <text class="brand-name" x="305" y="134" text-anchor="middle">NORVALE</text>

    <polygon class="promo-burst" fill="var(--yellow)" points="604,222 581,232 598.5,249.6 573.6,249.8 582.9,272.9 559.8,263.6 559.6,288.5 541.8,271 532,294 522.2,271 504.4,288.5 504.2,263.6 481.1,272.9 490.4,249.8 465.5,249.6 483,232 460,222 483,212.2 465.5,194.4 490.4,194.2 481.1,171.1 504.2,180.4 504.4,155.5 522.2,173 532,150 541.8,173 559.6,155.5 559.8,180.4 582.9,171.1 573.6,194.2 598.5,194.4 581,212.2"/>
    <text class="burst-text" text-anchor="middle">
      <tspan x="532" y="207">New Look -</tspan>
      <tspan x="532" y="225">Same Great</tspan>
      <tspan x="532" y="243">Taste!!</tspan>
    </text>

    <ellipse class="variant-oval" cx="410" cy="480" rx="218" ry="64" fill="var(--white)" stroke="var(--orange)" stroke-width="5"/>
    <text class="variant-main" x="405" y="480" text-anchor="middle">CREAMY</text>
    <text class="variant-sub" x="405" y="518" text-anchor="middle">PEANUT BUTTER</text>

    <text class="net-weight" x="110" y="569">200 GRAMS</text>
  </g>
</svg>
</body>
</html>
```